Slim Can Designs! Single Origin Coffee Cold Brew Coffee Cans

Amber Heron is a lifestyle brand with a focus on producing coffee. We need a three labels designed for our Cold Brew Cans. These will be 12 oz. slim cans for cold brew coffee. Each can will represent a different flavor profile tied to a virtue. Template Attached. We only have three products for cold brew cans. Please also review all the files included in our project for reference.
1. Gratitude : Toffee, Smokey, Chocolate
Things to include: Single Origin Coffee Dark Roast / Bold and Strong
2. Patience : Caramel, Chocolate, Dried Mango / Bright and Sparkling
Things to include: Single Origin Coffee Medium Roast
3. Kindness : Berry, Citrus, Floral / Smooth and Rich
Things to include: Single Origin Coffee Light Roast
All cans should include:
1. our logo. and brand colors.
2. all virtue icons if possible ?
3. Nutrition Label attached. Use this for all three, it may change but please use for placeholder.
4. Barcode
5. Net wt. 12oz
6. Ingredients : Single Origin Coffee, Water
7. BE KIND DRINK COFFEE
8. EST 2007
9. Roasted in Portland
10. Our business name and address:
Amber Heron Coffee Roasters
Portland, Oregon
web amberheronco.com
instagram amberheronco
11. Ethically Sourced Coffee Icon: if you can create one
12. Please recycle icon
13. Shake Lightly and Serve Chilled
14. Caffeine Content 200mg. : this might change between product but please use this as a placeholder for now.
15.

These designs should be cohesive and have some connection to our other brand element to tie together with our other current product designs. We are looking for sleek but fun and bold with colors and elements.

Target Market(s)

Mass market

Industry/Entity Type

Coffee

Font styles to use
Sans Serif
Other font styles liked:
• Please refer to our brand kit

Requirements
Must have
• Please refer to description
Nice to have

```html
<!DOCTYPE html>
<html lang="en">
<head>
<meta charset="utf-8">
<title>Amber Heron Cold Brew – Can Labels</title>
<link href="https://fonts.googleapis.com/css2?family=Montserrat:wght@400;500;600&family=Barlow+Condensed:wght@400;500;700&display=swap" rel="stylesheet">
<style>
  :root{
    --navy:#1f2a4a;
    --navy-deep:#171f38;
    --green:#4f8a7e;
    --cream:#f1d49d;
    --blush:#ecdcd6;
    --red:#c0384c;
    --gold:#e9c68c;
    --white:#ffffff;
    --page:#f1f1f1;
    --ink:#1f2a4a;
  }
  *{box-sizing:border-box;margin:0;padding:0}
  html,body{width:1200px;height:1102px;overflow:hidden}
  body{background:var(--page);position:relative;font-family:"Montserrat",sans-serif;color:var(--ink)}

  .can{position:absolute;top:256px;width:254px;height:600px;border-radius:14px;overflow:hidden;background:var(--body)}
  .can--gratitude{left:173px;--body:var(--green);--name-bg:var(--green);--name-color:var(--white);--notes-color:var(--white);--ribbon:var(--red);--ribbon-text:var(--white);--icon:var(--green)}
  .can--patience{left:483px;--body:var(--cream);--name-bg:var(--cream);--name-color:var(--navy);--notes-color:var(--navy);--ribbon:var(--green);--ribbon-text:var(--white);--icon:var(--gold)}
  .can--kindness{left:796px;--body:var(--blush);--name-bg:var(--blush);--name-color:var(--red);--notes-color:var(--navy);--ribbon:var(--gold);--ribbon-text:var(--navy);--icon:var(--red)}

  .pattern-band{position:absolute;left:0;right:0;top:376px;bottom:0;
    background:linear-gradient(135deg,var(--navy) 0%,#eadcd3 30%,var(--red) 50%,#eadcd3 65%,var(--green) 85%,var(--navy) 100%)}

  .panel{position:absolute;left:31px;width:200px;top:94px;height:210px;background:linear-gradient(160deg,var(--navy) 0%,var(--navy-deep) 100%)}

  .brand{position:absolute;left:0;right:0;top:22px;text-align:center;color:var(--white)}
  .brand__dot{display:block;width:14px;height:14px;border-radius:50%;background:var(--white);margin:0 auto 6px}
  .brand__name{font-weight:500;font-size:9px;line-height:9.5px;letter-spacing:.1px;text-transform:uppercase}
  .brand__tag{font-weight:500;font-size:4px;letter-spacing:1.6px;text-transform:uppercase;margin-top:1px}

  .virtue-icon{position:absolute;left:50%;top:96px;width:102px;height:102px;margin-left:-51px;border-radius:50%;background:var(--icon)}

  .label{position:absolute;left:18px;width:225px;top:300px;height:189px;background:var(--white);border-radius:3px}
  .name-box{position:absolute;left:13px;width:202px;top:2px;height:80px;background:var(--name-bg);text-align:center}
  .ribbon{position:absolute;left:50%;top:-6px;transform:translateX(-50%);background:var(--ribbon);color:var(--ribbon-text);
    font-family:"Barlow Condensed",sans-serif;font-weight:500;font-size:9px;letter-spacing:1px;padding:1px 12px;
    clip-path:polygon(0 0,100% 0,94% 50%,100% 100%,0 100%,6% 50%)}
  .virtue{font-family:"Montserrat",sans-serif;font-weight:500;font-size:27px;letter-spacing:.3px;color:var(--name-color);margin-top:18px;line-height:30px}
  .notes{font-family:"Barlow Condensed",sans-serif;font-weight:400;font-size:11px;letter-spacing:.4px;color:var(--notes-color);margin-top:6px;text-transform:uppercase}

  .roast{position:absolute;left:0;right:0;top:96px;text-align:center;font-family:"Barlow Condensed",sans-serif;font-weight:400;font-size:17px;letter-spacing:1.4px;color:var(--ink)}
  .rule{position:absolute;left:30px;right:26px;top:119px;border-top:1px solid var(--ink)}

  .facts{position:absolute;left:0;right:0;top:128px;height:38px;display:flex;align-items:center;justify-content:center;font-family:"Barlow Condensed",sans-serif}
  .facts__side{font-size:7px;width:38px;text-align:center}
  .facts__main{border-left:1px solid var(--ink);border-right:1px solid var(--ink);padding:0 13px;text-align:center;height:38px}
  .cold-brew{font-weight:700;font-size:18px;line-height:18px;letter-spacing:.3px}
  .style{font-size:8px;line-height:9px}
  .caffeine{font-size:4px;letter-spacing:.8px;text-transform:uppercase;margin-top:2px}
</style>
</head>
<body>

<article class="can can--gratitude">
  <div class="pattern-band" role="img" aria-label="Swirling pattern with Single Origin Coffee lettering"></div>
  <div class="panel">
    <div class="brand"><span class="brand__dot"></span><p class="brand__name">Amber Heron<br>Coffee Roasters</p><p class="brand__tag">Single Origin Coffee</p></div>
    <div class="virtue-icon" role="img" aria-label="Gratitude virtue icon"></div>
  </div>
  <div class="label">
    <div class="name-box">
      <span class="ribbon">ESDT&nbsp; 2007</span>
      <h2 class="virtue">GRATITUDE</h2>
      <p class="notes">Toffee ✦ Smokey ✦ Chocolate</p>
    </div>
    <p class="roast">DARK ROAST</p>
    <div class="rule"></div>
    <div class="facts">
      <span class="facts__side">12 OUNCES</span>
      <div class="facts__main"><p class="cold-brew">COLD BREW</p><p class="style">Bold &amp; Strong</p><p class="caffeine">Caffance contain 200 mg</p></div>
      <span class="facts__side">355 ML</span>
    </div>
  </div>
</article>

<article class="can can--patience">
  <div class="pattern-band" role="img" aria-label="Swirling pattern with Single Origin Coffee lettering"></div>
  <div class="panel">
    <div class="brand"><span class="brand__dot"></span><p class="brand__name">Amber Heron<br>Coffee Roasters</p><p class="brand__tag">Single Origin Coffee</p></div>
    <div class="virtue-icon" role="img" aria-label="Patience virtue icon"></div>
  </div>
  <div class="label">
    <div class="name-box">
      <span class="ribbon">ESDT&nbsp; 2007</span>
      <h2 class="virtue">PATIENCE</h2>
      <p class="notes">Caramel ✦ Chocolate ✦ Dried Mango</p>
    </div>
    <p class="roast">MEDIUM ROAST</p>
    <div class="rule"></div>
    <div class="facts">
      <span class="facts__side">12 OUNCES</span>
      <div class="facts__main"><p class="cold-brew">COLD BREW</p><p class="style">Bright and Sparkling</p><p class="caffeine">Caffance contain 200 mg</p></div>
      <span class="facts__side">355 ML</span>
    </div>
  </div>
</article>

<article class="can can--kindness">
  <div class="pattern-band" role="img" aria-label="Swirling pattern with Single Origin Coffee lettering"></div>
  <div class="panel">
    <div class="brand"><span class="brand__dot"></span><p class="brand__name">Amber Heron<br>Coffee Roasters</p><p class="brand__tag">Single Origin Coffee</p></div>
    <div class="virtue-icon" role="img" aria-label="Kindness virtue icon"></div>
  </div>
  <div class="label">
    <div class="name-box">
      <span class="ribbon">ESDT&nbsp; 2007</span>
      <h2 class="virtue">KINDNESS</h2>
      <p class="notes">Berry ✦ Citrus ✦ Floral</p>
    </div>
    <p class="roast">LIGHT ROAST</p>
    <div class="rule"></div>
    <div class="facts">
      <span class="facts__side">12 OUNCES</span>
      <div class="facts__main"><p class="cold-brew">COLD BREW</p><p class="style">Smooth and Rich</p><p class="caffeine">Caffance contain 200 mg</p></div>
      <span class="facts__side">355 ML</span>
    </div>
  </div>
</article>

</body>
</html>
```